Classy website for Corporate Entertainment - Action & Acrobatic Shows

12-Page Website to be coded using Wordpress!

We are "Velvet Summit Productions". We are all about providing 'experiences'! This website must be part of that experience :)

Please do not use our current website as inspiration for your design! We are looking for something new, and our business has outgrown that site (which was just for our shows) :)

We perform Action & Acrobatic Shows for corporate functions, as well as run Classes & Workshops from our Training Centre (Parkour, Acrobatics, etc), as well as Client Action Experiences and other services.

Example of our recent Morgan Vale 'Acrobatic Action Show' https://clipvault.example/watch/QxTr7nLpWzK

Our website must be super-classy/suave!! Needs to be heavily appealing to the Corporate community!

www.friendsphere.example/velvetsummitlive

Logo is available in the files below.
A series of photos have also been uploaded; please use any of these that you like throughout the design.

Menu Links from Home Page:
About Us (dropdown), Corporate Action Shows, Services (dropdown), Classes & Workshops (dropdown), The Ultimate Action Experience, Blog, Photos/Videos, Contact Us

PAGES:
- Home Page - must include a focus on Corporate Entertainment for the first glance, with information going down the page about our 4 major aspects: our Corporate Action Shows, Workshops & Classes, Services and Blog.

Required links on menu (menu does not necessarily have to be as a banner across the top - we are open to all ideas):

- Home Page

-"About Us" (dropdown with x2 pages "Our Shows" and "Our Team")

- Corporate Action Shows (x1 page)

- Services (dropdown with x3 pages "Action Showreels", and "Cosplay Competition Skits", and "Film & TV"

- Classes & Workshops (dropdown with x2 pages "Class Details & Prices" and "2016 Timetable"

- Ultimate Action Experience (x1 page with link to external website)

- Blog

- Videos & Photos or "See Us In Action" (x1 page)

- Contact Us

If you need more in-depth information into anything, please do not hesitate to send us a message!

Target Market(s)

Corporate (Classy)

Industry/Entity Type

Entertainment

Coding

Coded - Design and coding required

Number of Pages Required

5+ page

Requirements
Must have
• Website Coded via Wordpress

```html
<!DOCTYPE html>
<html lang="en">
<head>
<meta charset="utf-8">
<title>Velvet Summit Productions — Corporate Action Shows</title>
<link rel="stylesheet" href="https://fonts.googleapis.com/css2?family=Oswald:wght@400;500;600&family=Open+Sans:wght@400;600&display=swap">
<style>
  :root {
    --ink: #ffffff;
    --ink-soft: #e9dede;
    --ink-muted: #b9c0c6;
    --nav-bg: #3f4b56;
    --nav-line: #55616c;
    --rose: #9d5856;
    --rose-deep: #7d3f3f;
    --slate: #6c7278;
    --slate-deep: #4a5056;
    --night: #17191c;
    --panel: #2a2d31;
    --footer: #1f2932;
    --footer-deep: #161d24;
    --field: #2f3a44;
    --accent: #c8ccd0;
  }
  * { box-sizing: border-box; margin: 0; padding: 0; }
  html, body { width: 692px; height: 1200px; overflow: hidden; }
  body {
    font-family: "Open Sans", Arial, sans-serif;
    color: var(--ink);
    background: var(--night);
    font-size: 7px;
    line-height: 1.55;
  }
  .page { width: 692px; height: 1200px; position: relative; }

  /* Hero */
  .hero {
    height: 168px; position: relative;
    background:
      radial-gradient(ellipse at 30% 20%, rgba(214,120,70,.55), transparent 45%),
      radial-gradient(ellipse at 75% 25%, rgba(190,80,90,.45), transparent 45%),
      linear-gradient(180deg, #3a1d1c 0%, #4b3330 50%, #5e5350 100%);
  }
  .brand {
    position: absolute; left: 112px; top: 6px;
    display: flex; align-items: center; gap: 6px;
  }
  .brand-square { width: 20px; height: 20px; background: var(--ink); }
  .brand-name {
    font-family: "Oswald", Arial, sans-serif; font-weight: 500;
    font-size: 11px; line-height: 1.1; text-transform: uppercase;
    letter-spacing: .5px; width: 92px; color: var(--ink);
  }

  /* Navigation */
  .main-nav {
    height: 40px; background: var(--nav-bg);
    border-top: 1px solid var(--nav-line);
    display: flex; align-items: center; padding-left: 108px; gap: 13px;
  }
  .main-nav a {
    font-family: "Oswald", Arial, sans-serif; font-size: 6.6px;
    letter-spacing: .4px; color: var(--ink); text-decoration: none;
    text-transform: uppercase;
  }

  /* Feature sections */
  .feature { position: relative; }
  .feature-shows {
    height: 312px;
    background:
      radial-gradient(ellipse at 80% 30%, rgba(60,30,30,.35), transparent 55%),
      linear-gradient(180deg, var(--rose) 0%, var(--rose-deep) 100%);
  }
  .feature-stylised {
    height: 277px;
    background:
      radial-gradient(ellipse at 25% 40%, rgba(40,44,48,.45), transparent 55%),
      linear-gradient(180deg, var(--slate) 0%, var(--slate-deep) 100%);
  }
  .section-title {
    display: flex; align-items: center; gap: 9px;
    font-family: "Oswald", Arial, sans-serif; font-weight: 500;
    font-size: 22px; letter-spacing: .8px; text-transform: uppercase;
    position: absolute;
  }
  .title-square { width: 22px; height: 22px; background: var(--ink); }
  .feature-shows .section-title { left: 104px; top: 54px; }
  .feature-stylised .section-title { left: 365px; top: 47px; }
  .feature-copy { position: absolute; color: var(--ink-soft); }
  .feature-copy p { margin-bottom: 7px; }
  .feature-shows .feature-copy { left: 104px; top: 94px; width: 220px; }
  .feature-stylised .feature-copy { left: 370px; top: 96px; width: 218px; }

  .video { position: absolute; background: #111; }
  .feature-shows .video { left: 346px; top: 112px; width: 242px; height: 136px; }
  .feature-stylised .video { left: 108px; top: 98px; width: 244px; height: 140px; }
  .video-frame { position: absolute; inset: 0 0 14px 0; }
  .video-shows .video-frame { background: linear-gradient(135deg, #3b3634 0%, #6b6561 50%, #2a2625 100%); }
  .video-stylised .video-frame { background: linear-gradient(135deg, #2e3a4a 0%, #6e5a4c 50%, #3a3030 100%); }
  .video-controls { position: absolute; left: 0; right: 0; bottom: 0; height: 14px; }

  /* Recent events */
  .events-head {
    height: 58px; background: var(--night);
    display: flex; justify-content: center; align-items: center;
  }
  .events-head .section-title { position: static; }
  .events-grid { height: 160px; display: flex; }
  .event-tile { width: 138.4px; height: 160px; }
  .event-intro {
    background: var(--panel); padding: 24px 10px 0 10px;
    font-size: 6.3px; color: var(--ink-muted);
  }
  .event-intro h3 {
    font-family: "Oswald", Arial, sans-serif; font-weight: 500; font-size: 8.5px;
    color: var(--ink); letter-spacing: .4px; margin-bottom: 3px;
  }
  .event-meta { display: flex; gap: 10px; margin-top: 8px; align-items: center; }
  .event-meta span { display: flex; align-items: center; gap: 3px; }
  .event-1 { background: linear-gradient(160deg, #d6d8da 0%, #8e9296 55%, #3a3d40 100%); }
  .event-2 { background: radial-gradient(ellipse at 50% 60%, #3fb4c8 0%, #224a66 40%, #0d1420 80%); }
  .event-3 { background: linear-gradient(160deg, #4a3b34 0%, #c6b9ad 50%, #5d4a40 100%); }
  .event-4 { background: linear-gradient(160deg, #6a2a3a 0%, #d8a033 50%, #3a2a30 100%); }

  /* Footer */
  .site-footer {
    height: 163px; background: var(--footer); position: relative;
  }
  .footer-heading {
    font-family: "Oswald", Arial, sans-serif; font-weight: 500; font-size: 10px;
    letter-spacing: .5px; text-transform: uppercase; padding-bottom: 4px;
    border-bottom: 1px solid var(--nav-line); margin-bottom: 8px;
  }
  .footer-contact { position: absolute; left: 115px; top: 12px; width: 120px; }
  .contact-line { display: flex; align-items: center; gap: 6px; margin-bottom: 5px; font-size: 6.3px; color: var(--ink-muted); }
  .social { display: flex; gap: 6px; margin-top: 8px; }
  .social span { width: 9px; height: 9px; border-radius: 50%; background: var(--ink-muted); }
  .footer-brand {
    position: absolute; left: 280px; top: 54px;
    display: flex; align-items: center; gap: 7px;
  }
  .footer-brand .brand-square { width: 26px; height: 26px; background: var(--accent); }
  .footer-brand .brand-name { font-size: 13px; width: 100px; color: var(--accent); }
  .quick-contact { position: absolute; left: 473px; top: 12px; width: 116px; }
  .field {
    display: flex; align-items: center; gap: 5px; height: 13px;
    margin-bottom: 4px; font-size: 6px; color: var(--ink-muted);
  }
  .field label { width: 26px; }
  .field span { flex: 1; height: 11px; background: var(--field); }
  .field-message { height: 28px; align-items: flex-start; }
  .field-message span { height: 28px; }
  .submit {
    display: block; margin: 4px 0 0 auto; width: 40px; height: 13px;
    background: var(--nav-bg); color: var(--ink); border: 0;
    font-family: "Oswald", Arial, sans-serif; font-size: 6px; letter-spacing: .4px;
  }
  .copyright {
    height: 22px; background: var(--footer-deep);
    font-size: 5.8px; color: var(--ink-muted);
    display: flex; align-items: center; padding-left: 115px;
  }
</style>
</head>
<body>
<div class="page">

  <header class="hero" role="img" aria-label="Photo of a crowd dancing in a lit nightclub venue">
    <div class="brand">
      <span class="brand-square"></span>
      <span class="brand-name">Velvet Summit Productions</span>
    </div>
  </header>

  <nav class="main-nav">
    <a href="#">About Us</a>
    <a href="#">Corporate Action Shows</a>
    <a href="#">Services</a>
    <a href="#">Classes &amp; Workshops</a>
    <a href="#">The Ultimate Action Experience</a>
    <a href="#">Blog</a>
    <a href="#">Photos/Videos</a>
    <a href="#">Contact Us</a>
  </nav>

  <section class="feature feature-shows">
    <h2 class="section-title"><span class="title-square"></span>Custom Action Shows</h2>
    <div class="feature-copy">
      <p>Our performers bring cinematic fight scenes and daring acrobatics straight to your corporate stage, tailored to your theme and venue.</p>
      <p>Every show is choreographed around your brand story, so guests feel part of a live action film from start to finish.</p>
      <p>We handle rigging, lighting cues and safety planning, leaving your team free to enjoy the night with clients.</p>
      <p>From product launches to award galas, each routine is built to spark conversation long after the final bow.</p>
    </div>
    <div class="video video-shows">
      <div class="video-frame" role="img" aria-label="Video still of a performer mid-flip on stage"></div>
      <svg class="video-controls" viewBox="0 0 242 14" preserveAspectRatio="none">
        <rect width="242" height="14" fill="#1b1b1b"/>
        <polygon points="6,4 6,10 11,7" fill="#fff"/>
        <rect x="18" y="6" width="170" height="2" fill="#555"/>
        <rect x="18" y="6" width="60" height="2" fill="#5aa0d8"/>
        <rect x="200" y="4" width="8" height="6" fill="#bbb"/>
        <rect x="214" y="4" width="8" height="6" fill="#bbb"/>
        <rect x="228" y="4" width="8" height="6" fill="#bbb"/>
      </svg>
    </div>
  </section>

  <section class="feature feature-stylised">
    <h2 class="section-title"><span class="title-square"></span>Stylised Shows</h2>
    <div class="video video-stylised">
      <div class="video-frame" role="img" aria-label="Video still of a stylised combat scene with dramatic lighting"></div>
      <svg class="video-controls" viewBox="0 0 244 14" preserveAspectRatio="none">
        <rect width="244" height="14" fill="#1b1b1b"/>
        <polygon points="6,4 6,10 11,7" fill="#fff"/>
        <rect x="18" y="6" width="172" height="2" fill="#555"/>
        <rect x="18" y="6" width="44" height="2" fill="#5aa0d8"/>
        <rect x="202" y="4" width="8" height="6" fill="#bbb"/>
        <rect x="216" y="4" width="8" height="6" fill="#bbb"/>
        <rect x="230" y="4" width="8" height="6" fill="#bbb"/>
      </svg>
    </div>
    <div class="feature-copy">
      <p>Stylised shows blend martial arts, parkour and dance into polished pieces set to music and light.</p>
      <p>Choose a mood, from sleek spy thriller to futuristic battle, and our crew will design the look.</p>
      <p>Costumes, props and effects are matched to your event so every moment feels seamless and premium.</p>
    </div>
  </section>

  <section class="events">
    <div class="events-head">
      <h2 class="section-title"><span class="title-square"></span>Recent Events</h2>
    </div>
    <div class="events-grid">
      <article class="event-tile event-intro">
        <h3>OMNIS DOLOR REPELLENDUS</h3>
        <p>Highlights from our latest gala performance for a leading finance group.</p>
        <div class="event-meta">
          <span><svg width="6" height="6" viewBox="0 0 6 6"><rect x=".5" y="1" width="5" height="4.5" fill="none" stroke="#b9c0c6" stroke-width=".8"/></svg>12 Feb 2016</span>
          <span><svg width="6" height="6" viewBox="0 0 6 6"><path d="M1 1 L5 3 L1 5 Z" fill="#b9c0c6"/></svg>Read more</span>
        </div>
      </article>
      <div class="event-tile event-1" role="img" aria-label="Photo of acrobats performing a lift in black and white"></div>
      <div class="event-tile event-2" role="img" aria-label="Photo of a performer under blue stage lights"></div>
      <div class="event-tile event-3" role="img" aria-label="Photo of a fight scene performed at a corporate event"></div>
      <div class="event-tile event-4" role="img" aria-label="Photo of performers on a brightly decorated event set"></div>
    </div>
  </section>

  <footer class="site-footer">
    <div class="footer-contact">
      <h4 class="footer-heading">Contact Us</h4>
      <div class="contact-line">
        <svg width="7" height="8" viewBox="0 0 7 8"><path d="M3.5 0.5 C1.8 0.5 1 1.7 1 3 C1 4.8 3.5 7.5 3.5 7.5 C3.5 7.5 6 4.8 6 3 C6 1.7 5.2 0.5 3.5 0.5 Z" fill="#b9c0c6"/><circle cx="3.5" cy="3" r="1" fill="#1f2932"/></svg>
        18 Harbour Lane, Eastwood
      </div>
      <div class="contact-line">
        <svg width="7" height="8" viewBox="0 0 7 8"><path d="M1.5 0.8 L3 0.8 L3.5 2.6 L2.6 3.3 C3 4.3 3.7 5 4.7 5.4 L5.4 4.5 L7 5 L7 6.5 C4 7 0.8 4 1.5 0.8 Z" fill="#b9c0c6"/></svg>
        +61 2 5550 0184
      </div>
      <div class="contact-line">
        <svg width="7" height="8" viewBox="0 0 7 8"><rect x=".5" y="1.5" width="6" height="4.5" fill="none" stroke="#b9c0c6" stroke-width=".8"/><path d="M.5 1.5 L3.5 4 L6.5 1.5" fill="none" stroke="#b9c0c6" stroke-width=".8"/></svg>
        hello@velvetsummit.example
      </div>
      <div class="social"><span></span><span></span><span></span><span></span></div>
    </div>

    <div class="footer-brand">
      <span class="brand-square"></span>
      <span class="brand-name">Velvet Summit Productions</span>
    </div>

    <form class="quick-contact">
      <h4 class="footer-heading">Quick Contact</h4>
      <div class="field"><label>Name</label><span></span></div>
      <div class="field"><label>Email</label><span></span></div>
      <div class="field field-message"><label>Message</label><span></span></div>
      <button class="submit" type="button">SUBMIT</button>
    </form>
  </footer>

  <div class="copyright">© 2016 Velvet Summit Productions. All rights reserved.</div>

</div>
</body>
</html>
```